LumaWireHub full website re-design

I'm looking for a current, cool new design of my website, lumawirehub.com. We sell fiber optic cables and accessories. It hasn't been changed for over 10 years. I would like fresh ideas, not excessive pictures of cables. It has to be easy to navigate because we have over 5k products that we sell. The platform that our site is built on is Prestashop. I've attached many of our popular brands as well as some of our products so you can get an idea of what we sell. I also encourage you to go to our current website to see everything we offer. We are a high end brand and I want to give that impression. The winning designer will likely have ongoing work in the future because we will be making changes and additions to our site. Prestashop experience preferred! Be creative as you want. I would like banner images across the top as well.

Target Market(s)

Men 20-50

Industry/Entity Type

Technology

Coding

Coded - Design and coding required

Number of Pages Required

5+ page

Requirements
Must have
• https://www.vidstreamo.com/watch?v=Q4-RtPw7z2M
Should not have
• cartoons

```html
<!DOCTYPE html>
<html lang="en">
<head>
<meta charset="utf-8">
<title>LumaWireHub — Fiber Optic Cables</title>
<link href="https://fonts.googleapis.com/css2?family=Montserrat:wght@300;400;500;600;700&display=swap" rel="stylesheet">
<style>
:root{
  --maroon:#7b0e2c;
  --maroon-dark:#5e0a21;
  --ink:#222;
  --muted:#666;
  --line:#e3e3e3;
  --white:#fff;
  --hero-dark:#0b0a10;
  --teal:#3fb8b8;
  --teal-dark:#17686b;
  --orange:#e2682c;
}
*{box-sizing:border-box;margin:0;padding:0}
html,body{width:1200px;height:2608px;overflow:hidden;background:var(--white);font-family:"Montserrat",sans-serif;color:var(--ink)}
a{color:inherit;text-decoration:none}
.page{position:relative;width:1200px;height:2608px}

/* header */
.topbar{height:70px;display:flex;align-items:center;padding:0 112px;justify-content:space-between}
.brand{display:flex;align-items:center;gap:10px;font-weight:700;font-size:24px;color:var(--maroon)}
.brand .mark{width:18px;height:18px;background:var(--maroon)}
.search{display:flex;width:320px;height:30px;border:1px solid #bbb}
.search span{flex:1;font-size:11px;color:#999;padding:8px 10px}
.search i{width:32px;display:flex;align-items:center;justify-content:center;border-left:1px solid #bbb}
.user-links{display:flex;gap:24px;font-size:11px;color:var(--muted);align-items:center}
.user-links span{display:flex;align-items:center;gap:5px}
.mainnav{height:40px;background:var(--maroon);display:flex;align-items:center;justify-content:space-between;padding:0 112px;color:#fff;font-size:12px}
.mainnav ul{display:flex;gap:32px;list-style:none}
.mainnav .cats{background:var(--maroon-dark);height:40px;padding:0 22px;display:flex;align-items:center;gap:8px}

/* hero */
.hero{position:relative;height:700px;overflow:hidden;background:
  radial-gradient(ellipse 420px 260px at 92% 82%,#f06a1c 0%,rgba(200,40,30,.85) 35%,transparent 75%),
  radial-gradient(ellipse 380px 300px at 70% 95%,rgba(170,20,50,.9) 0%,transparent 70%),
  radial-gradient(ellipse 360px 260px at 8% 22%,#7a1236 0%,transparent 70%),
  radial-gradient(ellipse 300px 200px at 95% 15%,rgba(130,20,60,.7) 0%,transparent 70%),
  var(--hero-dark)}
.hero-art{position:absolute;left:500px;top:0;width:560px;height:560px;background:
  radial-gradient(ellipse 160px 110px at 30% 30%,#8fe6e2 0%,transparent 70%),
  radial-gradient(ellipse 200px 140px at 70% 55%,#5fd0cc 0%,transparent 70%),
  radial-gradient(ellipse 140px 260px at 50% 10%,#bfc7c8 0%,transparent 70%),
  radial-gradient(ellipse 320px 320px at 50% 50%,#2b9a9a 0%,rgba(20,70,75,.6) 60%,transparent 80%)}
.hero-copy{position:absolute;left:108px;top:208px;width:460px;color:#fff}
.hero-copy h1{font-size:31px;font-weight:700;margin-bottom:12px;white-space:nowrap}
.hero-copy p{font-size:12px;line-height:1.45;color:#e6e6e6;margin-bottom:26px;width:330px}
.btn{display:inline-block;background:var(--maroon);color:#fff;font-size:10px;font-weight:600;padding:9px 18px}

/* new arrivals */
.section-title{text-align:center;font-size:24px;font-weight:300;letter-spacing:.5px}
.arrivals{padding-top:86px}
.grid4{display:flex;justify-content:center;gap:118px;margin-top:40px}
.product{width:150px;text-align:center}
.product .photo{height:84px;position:relative;background:
  radial-gradient(ellipse 50px 24px at 50% 55%,#9aa0a4 0%,#cfd3d5 55%,transparent 80%),#fff}
.product:nth-child(3) .photo{background:radial-gradient(ellipse 55px 30px at 50% 55%,#3a3d40 0%,#a3a7aa 50%,transparent 80%),#fff}
.product:nth-child(4) .photo{background:radial-gradient(ellipse 44px 30px at 50% 55%,#b9a7b6 0%,#dcd6dc 55%,transparent 80%),#fff}
.product .tag{position:absolute;right:0;top:-12px;font-size:8px;color:#999}
.product .name{font-size:9px;color:var(--muted);margin-top:22px}
.product .price{font-size:12px;font-weight:600;margin:6px 0 8px}
.product .btn{width:100%;font-size:9px;padding:8px 0}
.dots{display:flex;justify-content:center;gap:8px;margin-top:70px}
.dots i{width:9px;height:9px;border-radius:50%;background:#c99aa7}
.dots i.on{background:var(--maroon)}

/* collections */
.collections{margin-top:96px}
.col-grid{display:flex;justify-content:center;gap:20px;margin-top:30px}
.collection{text-align:center}
.collection.teal{width:576px}
.collection.orange{width:380px}
.collection .photo{height:396px}
.collection.teal .photo{background:
  radial-gradient(ellipse 180px 120px at 45% 35%,#7fd8d4 0%,transparent 70%),
  linear-gradient(180deg,#e9eeee 0%,#cdd5d5 50%,#3fb3ad 62%,#2a9b95 78%,#f1f1f1 82%,#e8eaea 100%)}
.collection.orange .photo{background:
  radial-gradient(ellipse 120px 110px at 45% 35%,#b8c4c8 0%,transparent 70%),
  linear-gradient(180deg,#f3f1f0 0%,#dcd8d6 45%,#e8732f 62%,#d85b20 76%,#f3f1f0 82%,#ecebea 100%)}
.collection h3{font-size:19px;font-weight:500;margin-top:24px}
.collection p{font-size:11px;color:var(--muted);line-height:1.6;margin:10px 0 12px}

/* brands */
.brands{display:flex;justify-content:center;gap:110px;align-items:center;margin-top:150px;height:80px}
.brands span{font-size:20px;font-weight:600;color:#333}
.brands .square{display:flex;align-items:center;gap:8px}
.brands .square i{width:40px;height:40px;background:#111}

/* footer */
footer{position:absolute;left:0;top:2146px;width:1200px;height:462px;border-top:1px solid var(--line);padding:36px 112px 0}
.fcols{display:flex}
.fcol{font-size:10px;color:var(--muted);line-height:2}
.fcol h4{font-size:12px;color:var(--ink);font-weight:600;margin-bottom:6px}
.fcol.about{width:340px;line-height:1.8}
.fcol.products{width:296px}
.fcol.company{width:236px}
.fcol.about .brand{margin-bottom:20px}
.bottom{position:absolute;left:112px;right:112px;top:392px;display:flex;justify-content:space-between;font-size:9px;color:#888;align-items:center}
.cards{display:flex;gap:6px;align-items:center}
.cards i{width:34px;height:20px;border-radius:3px}
.cards i:nth-child(1){background:#1a3a8a}
.cards i:nth-child(2){background:#c43a2a}
.cards i:nth-child(3){background:#2a7ab8}
</style>
</head>
<body>
<div class="page">
  <header class="topbar">
    <div class="brand"><span class="mark"></span>LumaWireHub</div>
    <div class="search"><span>What are you looking for?</span><i><svg width="12" height="12" viewBox="0 0 12 12"><circle cx="5" cy="5" r="3.6" fill="none" stroke="#666" stroke-width="1.4"/><line x1="7.7" y1="7.7" x2="11" y2="11" stroke="#666" stroke-width="1.4"/></svg></i></div>
    <div class="user-links">
      <span><svg width="12" height="11" viewBox="0 0 12 11"><path d="M6 10 1.5 5.5A2.6 2.6 0 0 1 6 2a2.6 2.6 0 0 1 4.5 3.5Z" fill="none" stroke="#666"/></svg>Wishlist (0)</span>
      <span><svg width="12" height="11" viewBox="0 0 12 11"><path d="M1 1h2l1.5 6h5.5L11 3H4" fill="none" stroke="#666"/><circle cx="5" cy="9.5" r="1" fill="#666"/><circle cx="9.5" cy="9.5" r="1" fill="#666"/></svg>Shopping (0)</span>
    </div>
  </header>
  <nav class="mainnav">
    <ul><li>Line Card</li><li>Cost/Quote Buyers</li><li>Resellers</li><li>Custom Cable</li><li>Purchasing</li></ul>
    <div class="cats">Categories <svg width="12" height="10" viewBox="0 0 12 10"><path d="M0 1h12M0 5h12M0 9h12" stroke="#fff" stroke-width="1.4"/></svg></div>
  </nav>

  <section class="hero">
    <div class="hero-art" role="img" aria-label="Teal multimode fiber patch cable connectors glowing against a red and orange backdrop"></div>
    <div class="hero-copy">
      <h1>OM4 LC LC Fiber Patch Cable</h1>
      <p>OM4 LC LC Angle Fiber Patch Cable, 10Gb Plenum Duplex Multimode Fiber Jumper with bend-insensitive core for tight installs</p>
      <a class="btn" href="#">Shop Now</a>
    </div>
  </section>

  <section class="arrivals">
    <h2 class="section-title">New Arrivals</h2>
    <div class="grid4">
      <div class="product"><div class="photo" role="img" aria-label="Set of silver fiber adapters"><span class="tag">NEW</span></div><div class="name">Request quote quickly</div><div class="price">$36.00</div><a class="btn" href="#">ADD TO CART</a></div>
      <div class="product"><div class="photo" role="img" aria-label="Metal fiber coupler adapter"><span class="tag">NEW</span></div><div class="name">Request quote quickly</div><div class="price">$36.00</div><a class="btn" href="#">ADD TO CART</a></div>
      <div class="product"><div class="photo" role="img" aria-label="Black ST fiber connectors"><span class="tag">NEW</span></div><div class="name">Request quote quickly</div><div class="price">$36.00</div><a class="btn" href="#">ADD TO CART</a></div>
      <div class="product"><div class="photo" role="img" aria-label="Pink LC duplex connector"><span class="tag">NEW</span></div><div class="name">Request quote quickly</div><div class="price">$36.00</div><a class="btn" href="#">ADD TO CART</a></div>
    </div>
    <div class="dots"><i></i><i class="on"></i><i></i></div>
  </section>

  <section class="collections">
    <h2 class="section-title">Our Collections</h2>
    <div class="col-grid">
      <div class="collection teal"><div class="photo" role="img" aria-label="Teal plenum rated OM4 patch cable connectors with a teal cable band"></div><h3>FlexBend Fiber Patch Cables</h3><p>OM4 LC Fiber Patch Cable<br>FlexBend Plenum OM 50/125 Multimode</p><a class="btn" href="#">Read More</a></div>
      <div class="collection orange"><div class="photo" role="img" aria-label="Orange riser rated LC patch cable connectors with an orange cable band"></div><h3>LC Fiber Patch Cables</h3><p>LC LC Fiber Patch Cable<br>10Gb Duplex 62.5/125 Multimode</p><a class="btn" href="#">Read More</a></div>
    </div>
  </section>

  <div class="brands">
    <span>FlexBend</span><span>NarrowFit</span><span>ShieldCore Max</span><span class="square"><i></i>Onyx Optics</span>
  </div>

  <footer>
    <div class="fcols">
      <div class="fcol about">
        <div class="brand"><span class="mark"></span>LumaWireHub</div>
        LumaWireHub Sales Office | Warehouse<br>410 Harbor Loop, Suite 12<br>Brookvale, CA 90210 - USA<br><br>Hours: 8:00am - 5:00pm / Mon-Fri<br><br>Call us now: (555) 014-2290<br><br>Email: sales@lumawirehub.com
      </div>
      <div class="fcol products"><h4>Products</h4>FlexBend Fiber Patch Cables<br>OS2 Singlemode Patch Cables<br>OM4 Multimode Patch Cables<br>OM3 Multimode Patch Cables<br>OM2 Multimode Patch Cables<br>OM1 Multimode Patch Cables<br>Ultra OS2 Multimode Patch Cables<br>OM5 Multimode Patch Cables</div>
      <div class="fcol company"><h4>Our company</h4>Delivery<br>Legal Notice<br>Terms and conditions of use<br>About us<br>Secure payment<br>Contact us<br>Sitemap<br>Stores</div>
      <div class="fcol"><h4>Your account</h4>Personal info<br>Orders<br>Credit slips<br>Addresses</div>
    </div>
    <div class="bottom"><span>Copyright © 2020 - LumaWireHub, Inc. All Rights Reserved</span><div class="cards"><i></i><i></i><i></i><span>CA</span></div></div>
  </footer>
</div>
</body>
</html>
```